Brennick Drilling Inc. Business card design

Business card design for "Brennick Drilling Inc. - Directional Drilling Services"

Address is:

Brennick Drilling Inc.
512 - 73 Tarvel Crescent SW
Calgary, Alberta, Canada
T2K 4P8

Please incorporate the logo design into the card, thank you.

Target Market(s)

Oil & Gas and Drilling

Industry/Entity Type

Business

```html
<!DOCTYPE html>
<html lang="en">
<head>
<meta charset="utf-8">
<title>Brennick Drilling Inc. — Business Card Concepts</title>
<link rel="stylesheet" href="https://fonts.googleapis.com/css2?family=Archivo:wght@600;700&family=Archivo+Narrow:wght@700&display=swap">
<style>
  :root {
    --red: #d9201b;
    --black: #111111;
    --white: #ffffff;
    --paper: #ffffff;
    --ghost: #ececec;
    --ghost-text: #e2e2e2;
    --shadow: rgba(0, 0, 0, 0.38);
  }
  * { box-sizing: border-box; margin: 0; padding: 0; }
  html, body { width: 1200px; height: 900px; overflow: hidden; background: var(--paper); }
  .sheet { position: relative; width: 1200px; height: 900px; }

  .card {
    position: absolute;
    background: var(--white);
    box-shadow: 0 10px 12px -2px var(--shadow);
    overflow: visible;
  }
  .card svg.art { position: absolute; left: 0; top: 0; }

  /* brand lockup */
  .brand {
    position: absolute;
    display: flex; flex-direction: column; align-items: center;
    transform: translateX(-50%);
  }
  .brand-dot {
    width: 22px; height: 22px; border-radius: 50%;
    border: 3px solid var(--red);
    margin-bottom: 6px;
  }
  .brand-name {
    font-family: "Archivo", sans-serif;
    font-weight: 700;
    font-size: 8.5px;
    letter-spacing: 0.9px;
    color: var(--black);
    white-space: nowrap;
    text-transform: uppercase;
  }
  .brand-ghost {
    position: absolute;
    display: flex; flex-direction: column; align-items: center;
    transform: translate(-50%, -50%);
  }
  .brand-ghost .ring {
    width: 104px; height: 104px; border-radius: 50%;
    border: 5px solid var(--ghost);
  }
  .brand-ghost .brand-name {
    position: absolute; top: 46px; color: var(--ghost-text); font-size: 8px;
  }

  /* address */
  .address {
    position: absolute;
    font-family: "Archivo Narrow", sans-serif;
    font-weight: 700;
    font-size: 7px;
    line-height: 10px;
    color: var(--black);
    white-space: nowrap;
  }
  .address.caps { text-transform: uppercase; }
  .address.red { color: var(--red); }
  .address.light { color: var(--white); }
  .address.center { text-align: center; transform: translateX(-50%); }

  .address-block {
    position: absolute;
    display: flex; align-items: flex-start; gap: 12px;
  }
  .address-block .address { position: static; }
  .address.large { font-family: "Archivo", sans-serif; font-size: 9px; line-height: 11px; }
  .address-rule { width: 3px; height: 38px; margin-top: 3px; background: var(--black); }

  .band { position: absolute; left: 0; width: 100%; }
  .band.red { background: var(--red); }
  .band.black { background: var(--black); }

  .frame { border: 9px solid var(--red); }
</style>
</head>
<body>
<main class="sheet">

  <!-- Column one -->
  <section class="card" style="left:213px;top:8px;width:279px;height:154px;">
    <svg class="art" width="279" height="154" viewBox="0 0 279 154">
      <polygon points="80,154 88,142 191,142 199,154" fill="var(--black)"/>
    </svg>
    <div class="brand" style="left:140px;top:52px;">
      <span class="brand-dot"></span>
      <span class="brand-name">Brennick Drilling Inc.</span>
    </div>
  </section>

  <section class="card" style="left:213px;top:192px;width:279px;height:155px;">
    <svg class="art" width="279" height="160" viewBox="0 -5 279 160" style="top:-5px">
      <polygon points="80,-4 198,-4 190,8 88,8" fill="var(--red)"/>
    </svg>
    <div class="brand-ghost" style="left:138px;top:78px;">
      <span class="ring"></span>
      <span class="brand-name">Brennick</span>
    </div>
    <p class="address caps" style="left:9px;top:117px;">512 - 73 Tarvel Crescent SW<br>Calgary, Alberta, Canada<br>T2K 4P8</p>
  </section>

  <section class="card" style="left:213px;top:378px;width:279px;height:155px;">
    <svg class="art" width="279" height="155" viewBox="0 0 279 155">
      <path d="M0,108 C60,120 130,150 195,140 C235,134 245,118 279,124 L279,155 L0,155 Z" fill="var(--black)"/>
      <path d="M0,108 C60,120 130,150 195,140 C235,134 245,118 279,124" fill="none" stroke="var(--red)" stroke-width="4"/>
    </svg>
    <div class="brand" style="left:140px;top:55px;">
      <span class="brand-dot"></span>
      <span class="brand-name">Brennick Drilling Inc.</span>
    </div>
  </section>

  <section class="card" style="left:213px;top:557px;width:279px;height:157px;">
    <div class="address-block" style="left:12px;top:67px;">
      <p class="address large">512 - 73 Tarvel Crescent SW<br>Calgary, Alberta, Canada<br>T2K 4P8</p>
      <span class="address-rule"></span>
    </div>
    <div class="band red" style="top:134px;height:7px;"></div>
    <div class="band black" style="top:141px;height:16px;"></div>
  </section>

  <section class="card frame" style="left:213px;top:739px;width:279px;height:156px;">
    <div class="brand" style="left:131px;top:47px;">
      <span class="brand-dot"></span>
      <span class="brand-name">Brennick Drilling Inc.</span>
    </div>
  </section>

  <!-- Column two -->
  <section class="card" style="left:517px;top:8px;width:279px;height:154px;">
    <svg class="art" width="279" height="158" viewBox="0 -4 279 158" style="top:-4px">
      <polygon points="97,-3 183,-3 178,8 102,8" fill="var(--red)"/>
      <polygon points="0,130 97,130 105,142 176,142 184,130 279,130 279,154 0,154" fill="var(--red)"/>
    </svg>
    <div class="brand" style="left:133px;top:50px;">
      <span class="brand-dot"></span>
      <span class="brand-name">Brennick Drilling Inc.</span>
    </div>
  </section>

  <section class="card" style="left:511px;top:192px;width:279px;height:155px;">
    <svg class="art" width="279" height="155" viewBox="0 0 279 155">
      <polygon points="0,34 11,46 11,108 0,118" fill="var(--black)"/>
    </svg>
    <p class="address caps red" style="left:22px;top:62px;">512 - 73 Tarvel Crescent SW<br>Calgary, Alberta, Canada<br>T2K 4P8</p>
  </section>

  <section class="card" style="left:511px;top:378px;width:279px;height:155px;">
    <div class="band red" style="top:0;height:40px;"></div>
    <div class="band red" style="top:115px;height:40px;"></div>
    <div class="brand" style="left:139px;top:52px;">
      <span class="brand-dot"></span>
      <span class="brand-name">Brennick Drilling Inc.</span>
    </div>
  </section>

  <section class="card" style="left:511px;top:555px;width:279px;height:156px;">
    <div class="band red" style="top:55px;height:50px;"></div>
    <p class="address light center" style="left:139px;top:63px;">512 - 73 Tarvel Crescent SW<br>Calgary, Alberta, Canada<br>T2K 4P8</p>
  </section>

  <section class="card frame" style="left:511px;top:730px;width:279px;height:156px;">
    <span style="position:absolute;left:36px;top:70px;width:189px;height:1.5px;background:var(--black);"></span>
    <p class="address center" style="left:130px;top:78px;">512 - 73 Tarvel Crescent SW<br>Calgary, Alberta, Canada<br>T2K 4P8</p>
  </section>

  <!-- Column three -->
  <section class="card" style="left:819px;top:8px;width:158px;height:276px;">
    <div class="brand" style="left:79px;top:74px;">
      <span class="brand-dot"></span>
      <span class="brand-name">Brennick Drilling Inc.</span>
    </div>
    <div class="band red" style="top:232px;height:44px;"></div>
  </section>

  <section class="card" style="left:819px;top:298px;width:158px;height:280px;">
    <div class="brand-ghost" style="left:79px;top:96px;">
      <span class="ring"></span>
      <span class="brand-name">Brennick</span>
    </div>
    <p class="address" style="left:10px;top:224px;">512 - 73 Tarvel Crescent SW<br>Calgary, Alberta, Canada<br>T2K 4P8</p>
    <div class="band red" style="top:268px;height:12px;"></div>
  </section>

  <section class="card" style="left:822px;top:611px;width:157px;height:276px;">
    <div class="brand" style="left:79px;top:45px;">
      <span class="brand-dot"></span>
      <span class="brand-name">Brennick Drilling Inc.</span>
    </div>
    <p class="address" style="left:10px;top:236px;">512 - 73 Tarvel Crescent SW<br>Calgary, Alberta, Canada<br>T2K 4P8</p>
  </section>

</main>
</body>
</html>
```